Attorney At Law Card Design

I am an attorney. I need something simple but elegant with nice conservative colors. The design should communicate competence, and confidence. I specialize in Personal Injury and Criminal Defense Work.

Industry/Entity Type

Conservative

Contact Information for Business Card

Velandro Law Firm
2837 Birchwell Ave.
McAllen, TX 78504

Rodolfo "Rudy" Velandro
956-413-2716 Tel.
956-413-2719 Fax
956-582-4130 Cell

Justice for All

```html
<!DOCTYPE html>
<html lang="en">
<head>
<meta charset="utf-8">
<title>Velandro Law Firm – Business Card</title>
<link rel="stylesheet" href="https://fonts.googleapis.com/css2?family=Crimson+Text:wght@600&family=PT+Sans+Narrow&display=swap">
<style>
  :root {
    --page-bg: #ece8e2;
    --card-white: #ffffff;
    --ink: #111111;
    --band-red: #c0252e;
    --band-text: #ffffff;
  }
  html, body {
    margin: 0;
    padding: 0;
    width: 1200px;
    height: 797px;
    overflow: hidden;
    background: var(--page-bg);
  }
  .business-card {
    position: absolute;
    left: 60px;
    top: 75px;
    width: 1080px;
    height: 648px;
    background: var(--card-white);
    box-shadow: 0 4px 14px rgba(0,0,0,0.18);
    overflow: hidden;
  }
  .firm-name {
    position: absolute;
    left: 0;
    width: 100%;
    top: 245px;
    margin: 0;
    text-align: center;
    font-family: "Crimson Text", Georgia, serif;
    font-weight: 600;
    font-size: 92px;
    line-height: 1;
    color: var(--ink);
    letter-spacing: 0.5px;
  }
  .practice-areas {
    position: absolute;
    left: 0;
    width: 100%;
    top: 365px;
    margin: 0;
    text-align: center;
    font-family: "Crimson Text", Georgia, serif;
    font-weight: 600;
    font-size: 34px;
    line-height: 1;
    color: var(--ink);
  }
  .contact-band {
    position: absolute;
    left: 0;
    bottom: 0;
    width: 100%;
    height: 178px;
    background: var(--band-red);
    font-family: "PT Sans Narrow", "Arial Narrow", sans-serif;
    color: var(--band-text);
    font-size: 27px;
    line-height: 44px;
  }
  .office-details {
    position: absolute;
    left: 32px;
    top: 62px;
  }
  .phone-lines {
    position: absolute;
    right: 80px;
    top: 18px;
    font-size: 27px;
  }
</style>
</head>
<body>
  <div class="business-card">
    <h1 class="firm-name">Velandro Law Firm</h1>
    <p class="practice-areas">Specialized in Personal Injury and Criminal Defense</p>
    <div class="contact-band">
      <div class="office-details">
        Velandro Law Firm 2837 Birchwell Ave. McAllen,<br>
        TX 78504 Rodolfo "Rudy" Velandro 956-582-4130
      </div>
      <div class="phone-lines">
        Tel. 956-413-2716<br>
        Fax 956-413-2719
      </div>
    </div>
  </div>
</body>
</html>
```